Business Card design, larkwell shipping

I started a container shipping company which specialized in export of cars, motorcycles, boats and general cargo overseas. I need a business card that stands out of the pack and gives clients an idea of what I do. I have attached a sample that someone designed for me but I don't think its the right fit. However the info on it is accurate so can be used right on new card.
Updates

Reason: I would like my new logo which is being designed on PLANOVISTRA.COM as well to be implemented into my business card.

Industry/Entity Type

Shipping

```html
<!DOCTYPE html>
<html lang="en">
<head>
<meta charset="utf-8">
<title>Larkwell Shipping – Business Card</title>
<link rel="stylesheet" href="https://fonts.googleapis.com/css2?family=Open+Sans:ital,wght@0,400;0,600;0,700;1,700&display=swap">
<style>
  :root {
    --page: #ecebe8;
    --card: #ffffff;
    --blue: #1a94d8;
    --gold: #e9c41c;
    --gold-deep: #d8ab1e;
    --ink: #1d1d1d;
    --rule: #9a9a9a;
  }
  * { box-sizing: border-box; margin: 0; padding: 0; }
  html, body { width: 957px; height: 1200px; overflow: hidden; }
  body {
    background: var(--page);
    font-family: "Open Sans", Arial, sans-serif;
    color: var(--ink);
    position: relative;
  }
  .card {
    position: absolute;
    width: 799px;
    height: 468px;
    background: var(--card);
    box-shadow: 0 4px 14px rgba(0,0,0,.18);
    overflow: hidden;
  }
  .card--front { left: 80px; top: 76px; }
  .card--back { left: 83px; top: 651px; height: 467px; }

  .brand {
    position: absolute;
    display: flex;
    align-items: center;
    gap: 10px;
    font-weight: 700;
    color: var(--blue);
    white-space: nowrap;
  }
  .brand__mark { width: 22px; height: 22px; background: var(--gold); }
  .card--front .brand { left: 55px; top: 130px; font-size: 30px; }
  .card--back .brand { left: 0; right: 0; top: 220px; justify-content: center; font-size: 40px; }
  .card--back .brand__mark { width: 28px; height: 28px; }

  .text { position: absolute; font-size: 18px; line-height: 1.5; white-space: nowrap; }
  .mobile { left: 83px; top: 200px; }
  .person { right: 60px; top: 120px; text-align: right; }
  .person__name { font-size: 25px; font-weight: 700; font-style: italic; color: var(--gold-deep); line-height: 1.3; }
  .person__title { font-size: 18px; }
  .address { left: 55px; top: 308px; }
  .email { right: 60px; top: 308px; }
  .wave { position: absolute; left: 0; bottom: 0; width: 799px; height: 140px; }
  .extension { right: 38px; top: 413px; color: #fff; font-weight: 700; font-size: 18px; }

  .web { left: 0; right: 0; top: 285px; text-align: center; }
  .stripes { position: absolute; left: 0; right: 0; top: 385px; }
  .stripes__blue { height: 5px; background: var(--blue); }
  .stripes__gold { height: 4px; background: var(--gold); }
  .offices {
    position: absolute; left: 0; right: 0; top: 415px;
    display: flex; justify-content: center; list-style: none; font-size: 18px;
  }
  .offices li { padding: 0 12px; border-left: 1px solid var(--rule); line-height: 1.2; }
  .offices li:first-child { border-left: none; }
</style>
</head>
<body>
  <section class="card card--front" aria-label="Card front">
    <div class="brand"><span class="brand__mark"></span>Larkwell Shipping</div>
    <p class="text mobile">Mobile 1-212-555-0148</p>
    <div class="text person">
      <p class="person__name">Marek Olsen</p>
      <p class="person__title">Chief Operating Officer</p>
    </div>
    <p class="text address">2200 Harbor Road Unit 4b<br>Bayview,NJ 07099</p>
    <p class="text email">Marek@larkwellgroup.com</p>
    <svg class="wave" viewBox="0 0 799 140" preserveAspectRatio="none" aria-hidden="true">
      <defs>
        <linearGradient id="goldBand" x1="0" y1="0" x2="0" y2="1">
          <stop offset="0" stop-color="#f0d21a"/>
          <stop offset="1" stop-color="#d8ab1e"/>
        </linearGradient>
      </defs>
      <path d="M0 82 C 160 92, 260 30, 420 12 C 560 -2, 700 4, 799 14 L799 140 L0 140 Z" fill="var(--blue)"/>
      <path d="M0 92 C 170 100, 270 42, 430 26 C 570 12, 700 18, 799 26 L799 140 L0 140 Z" fill="url(#goldBand)"/>
    </svg>
    <p class="text extension">Direct Extension# 1-718-555-0172</p>
  </section>

  <section class="card card--back" aria-label="Card back">
    <div class="brand"><span class="brand__mark"></span>Larkwell Shipping</div>
    <p class="text web">www.larkwellgroup.com</p>
    <div class="stripes"><div class="stripes__blue"></div><div class="stripes__gold"></div></div>
    <ul class="offices">
      <li>New York</li><li>Savannah</li><li>Miami</li><li>Houston</li><li>Los Angeles</li><li>Seattle</li>
    </ul>
  </section>
</body>
</html>
```